Custom Truck shop New Business Card design

double sided business card including my new logo, brand colors and picking a font I attached, clean and modern look. I attached the old card for some reference. and would like to include the picture of the white truck attached. I would also like to have it with one of my employees info as well. (same info except name and title Brin Tolvay Service Writer)

Dale Porvick
Owner

address
48310 E Calloway Ridge Rd S
STE 217
Marsh Hollow, CO 80219

phone 720-555-0184

email dale@brokenspurrigs.example

website brokenspurrgis.example

social @brokenspurrigs

Target Market(s)

men 18-60

Industry/Entity Type

Automotive

Contact Information for Business Card

Dale Porvick Owner address 48310 E Calloway Ridge Rd S STE 217 Marsh Hollow, CO 80219 phone 720-555-0184 email dale@brokenspurrigs.example website brokenspurrgis.example social @brokenspurrigs

Font styles to use
Other font styles liked:
• fonts attached

Requirements
Must have
• new logo, orange #FC68D, Charcoal #333333
Nice to have
• the white truck

```html
<!DOCTYPE html>
<html lang="en">
<head>
<meta charset="utf-8">
<title>Broken Spur Rigs – Business Card</title>
<link href="https://fonts.googleapis.com/css2?family=Montserrat:wght@700&family=Oswald:wght@300;400&display=swap" rel="stylesheet">
<style>
  :root {
    --orange: #fc6821;
    --charcoal: #333333;
    --dark: #2b2b2b;
    --white: #ffffff;
    --backdrop: #e6e6e6;
    --photo-light: #e0672a;
    --photo-dark: #3a1d0e;
  }
  * { margin: 0; padding: 0; box-sizing: border-box; }
  html, body { width: 1200px; height: 1200px; overflow: hidden; background: var(--backdrop); }
  .card {
    position: absolute; left: 274px; width: 652px; height: 372px; overflow: hidden;
  }
  .card-front { top: 182px; background: var(--white); }
  .card-back { top: 645px; background: var(--charcoal); }
  .front-shapes { position: absolute; inset: 0; }
  .brand-mark {
    position: absolute; left: 97px; top: 22px; width: 64px; height: 64px;
    border-radius: 50%; background: var(--charcoal); border: 3px solid var(--orange);
  }
  .brand-name {
    position: absolute; font-family: "Montserrat", sans-serif; font-weight: 700;
    white-space: nowrap; letter-spacing: 0.5px;
  }
  .card-front .brand-name {
    left: 0; width: 258px; top: 92px; text-align: center; font-size: 21px; color: var(--charcoal);
  }
  .holder {
    position: absolute; right: 18px; top: 88px; text-align: right;
    font-family: "Montserrat", sans-serif; font-weight: 700; color: var(--white);
  }
  .holder-name { font-size: 23px; line-height: 28px; }
  .holder-title { font-size: 17px; line-height: 22px; }
  .contact-list {
    position: absolute; left: 28px; top: 176px; list-style: none;
    font-family: "Oswald", sans-serif; font-weight: 300; font-size: 17px; color: var(--charcoal);
  }
  .contact-item { display: flex; align-items: flex-start; line-height: 21px; }
  .contact-item + .contact-item { margin-top: 5px; }
  .contact-item.address { margin-bottom: 24px; }
  .contact-icon { width: 12px; height: 12px; margin: 4px 10px 0 0; flex: none; fill: var(--orange); }
  .back-mark {
    position: absolute; left: 279px; top: 109px; width: 94px; height: 94px;
    border-radius: 50%; border: 4px solid var(--white);
  }
  .card-back .brand-name {
    left: 0; width: 100%; top: 220px; text-align: center; font-size: 30px; color: var(--white);
  }
  .social-handle {
    position: absolute; left: 0; width: 100%; top: 312px; text-align: center;
    font-family: "Oswald", sans-serif; font-weight: 400; font-size: 20px; color: var(--white);
  }
</style>
</head>
<body>
  <section class="card card-front">
    <svg class="front-shapes" width="652" height="372" viewBox="0 0 652 372">
      <defs>
        <linearGradient id="truck-tone" x1="0" y1="0" x2="1" y2="1">
          <stop offset="0" stop-color="var(--photo-light)"/>
          <stop offset="0.55" stop-color="#a4461a"/>
          <stop offset="1" stop-color="var(--photo-dark)"/>
        </linearGradient>
      </defs>
      <rect x="0" y="361" width="256" height="11" fill="var(--orange)"/>
      <polygon points="248,0 437,0 378,116" fill="var(--dark)"/>
      <polygon points="437,0 652,0 652,372 253,372 378,116" fill="url(#truck-tone)" role="img" aria-label="Photo of a lifted white pickup truck, orange toned"/>
    </svg>
    <div class="brand-mark"></div>
    <div class="brand-name">BROKEN SPUR RIGS</div>
    <div class="holder">
      <div class="holder-name">DALE PORVICK</div>
      <div class="holder-title">OWNER</div>
    </div>
    <ul class="contact-list">
      <li class="contact-item address">
        <svg class="contact-icon" viewBox="0 0 12 12"><path d="M6 0a4.2 4.2 0 0 0-4.2 4.2C1.8 7.3 6 12 6 12s4.2-4.7 4.2-7.8A4.2 4.2 0 0 0 6 0zm0 5.9a1.7 1.7 0 1 1 0-3.4 1.7 1.7 0 0 1 0 3.4z"/></svg>
        <span>48310 E Calloway Ridge Rd S<br>STE 217, Marsh Hollow, CO 80219</span>
      </li>
      <li class="contact-item">
        <svg class="contact-icon" viewBox="0 0 12 12"><path d="M2.4 0.5 4.3 2.9 3.4 4.3c.7 1.6 2.2 3.1 4 4l1.4-.9 2.4 1.9-.9 2.1C5 11.3.6 6.9.4 1.3z"/></svg>
        <span>720-555-0184</span>
      </li>
      <li class="contact-item">
        <svg class="contact-icon" viewBox="0 0 12 12"><path d="M0 2.5h12v7H0z M0 2.5 6 6.8 12 2.5" stroke="var(--white)" stroke-width="0.8"/></svg>
        <span>dale@brokenspurrigs.example</span>
      </li>
      <li class="contact-item">
        <svg class="contact-icon" viewBox="0 0 12 12"><circle cx="6" cy="6" r="5.5"/><path d="M0.5 6h11M6 0.5v11M2 3h8M2 9h8" stroke="var(--white)" stroke-width="0.7" fill="none"/></svg>
        <span>www.brokenspurrgis.example</span>
      </li>
    </ul>
  </section>

  <section class="card card-back">
    <div class="back-mark"></div>
    <div class="brand-name">BROKEN SPUR RIGS</div>
    <div class="social-handle">@brokenspurrigs</div>
  </section>
</body>
</html>
```